GUARANTEE PAY GIFT CARD DESIGN

This is a GIFT BONUS CARD

SIZE: 3.5INCH x 2INCH, 8.9cm x 5.1cm, DOUBLE SIDE
Orange must be used as an accent or primary colour.
#F37021, CMYK 0, 54, 86, 5

"BONUS CARD" AND "$20" MUST BE PART OF THE DESIGN.

Please see the attached logo
DO NOT use ribbons or gift box illustrations in the design.

***Terms and conditions must be on the back side of the card-
"No Cash Value. Card valid from 1/2/2024 to 3/31/2024. Valid for Harlow Creek location only. Valid for Dine-in only. Not valid for online togo, delivery, or special events. "

Target Market(s)

40-60 YEARS OLD

Industry/Entity Type

Modern casual malaysian restaurant

Requirements
Must have
• ORANGE COLOUR, BONUS CARD, $20
Should not have
• Ribbons, gift box, CHOPSTICKS, BOWL, NOODLES, CHARATER ILLUSTRATIONS.

```html
<!DOCTYPE html>
<html lang="en">
<head>
<meta charset="utf-8">
<title>Kopi Lane Bonus Card</title>
<link rel="stylesheet" href="https://fonts.googleapis.com/css2?family=Lato:wght@400;900&family=Josefin+Sans:wght@600&display=swap">
<style>
  :root {
    --backdrop: #8f8f8f;
    --orange: #f79633;
    --ink: #000000;
    --charcoal: #333333;
  }
  * { margin: 0; padding: 0; box-sizing: border-box; }
  html, body { width: 1200px; height: 1200px; overflow: hidden; }
  body {
    background: var(--backdrop);
    position: relative;
    font-family: "Lato", sans-serif;
    color: var(--ink);
  }
  .card {
    position: absolute;
    left: 250px;
    width: 700px;
    height: 399px;
    background: var(--orange);
    border-radius: 34px;
    overflow: hidden;
    box-shadow: 0 2px 4px rgba(0,0,0,0.15);
  }
  .card--front { top: 170px; }
  .card--back { top: 631px; }

  .value-disc {
    position: absolute;
    left: 440px;
    top: -33px;
    width: 310px;
    height: 310px;
  }
  .value {
    position: absolute;
    left: 472px;
    top: 44px;
    color: var(--orange);
    font-weight: 900;
    line-height: 1;
    display: flex;
    align-items: flex-start;
  }
  .value__currency { font-size: 56px; margin-top: 6px; margin-right: 4px; }
  .value__amount { font-size: 140px; letter-spacing: -2px; }

  .brand-name--front {
    position: absolute;
    left: 67px;
    top: 115px;
    font-family: "Josefin Sans", sans-serif;
    font-weight: 600;
    font-size: 32px;
    letter-spacing: 3px;
    line-height: 1;
    white-space: nowrap;
  }

  .card-title {
    position: absolute;
    left: 67px;
    top: 273px;
    font-size: 88px;
    line-height: 1;
    letter-spacing: -1px;
    white-space: nowrap;
  }
  .card-title__bold { font-weight: 900; }
  .card-title__light { font-weight: 400; }

  .brand-name--back {
    position: absolute;
    left: 0;
    right: 0;
    top: 72px;
    text-align: center;
    font-family: "Josefin Sans", sans-serif;
    font-weight: 600;
    font-size: 56px;
    letter-spacing: 4px;
    line-height: 1;
  }

  .stripe {
    position: absolute;
    left: 0;
    top: 198px;
    width: 100%;
    height: 108px;
    background: var(--ink);
  }
  .stripe__shine {
    position: absolute;
    left: 0;
    top: 5px;
    width: 100%;
    height: 97px;
    background: linear-gradient(100deg, var(--charcoal) 0%, var(--charcoal) 47%, var(--ink) 55%, var(--ink) 100%);
  }

  .terms {
    position: absolute;
    left: 0;
    right: 0;
    top: 336px;
    text-align: center;
    font-size: 13.5px;
    line-height: 17px;
  }
</style>
</head>
<body>

  <section class="card card--front">
    <svg class="value-disc" viewBox="0 0 310 310" aria-hidden="true">
      <defs>
        <linearGradient id="disc-shine" x1="0" y1="0" x2="1" y2="0.35">
          <stop offset="0" stop-color="#333333"/>
          <stop offset="0.5" stop-color="#333333"/>
          <stop offset="0.58" stop-color="#000000"/>
          <stop offset="1" stop-color="#000000"/>
        </linearGradient>
      </defs>
      <circle cx="155" cy="155" r="153" fill="#000000"/>
      <circle cx="155" cy="155" r="149" fill="url(#disc-shine)"/>
    </svg>
    <div class="value"><span class="value__currency">$</span><span class="value__amount">20</span></div>

    <div class="brand-name--front">KOPI LANE</div>

    <h1 class="card-title"><span class="card-title__bold">BONUS</span> <span class="card-title__light">CARD</span></h1>
  </section>

  <section class="card card--back">
    <div class="brand-name--back">KOPI LANE</div>
    <div class="stripe"><div class="stripe__shine"></div></div>
    <p class="terms">
      No Cash Value. Card valid from 1/2/2024 to 3/31/2024. Valid for Harlow Creek location only.<br>
      Valid for Dine-in only. Not valid for online togo, delivery, or special events.
    </p>
  </section>

</body>
</html>
```